Awesome photographers card for an awesome new business

Double sided business card Black background and silver logo in middle on one side. Details on otherside. please keep it simple

Photographer

Gavin Tolley
0482615073
GavinTolleyPhotography82@lumenpost.com
www.GavinTolleyPhotography.com.au
Instagram _Gavin_tolley

Requirements
Must have
• My logo in Silver
• please use instagram logo instead of "Instagram"

```html
<!DOCTYPE html>
<html lang="en">
<head>
<meta charset="utf-8">
<title>Gavin Tolley — Photographer Business Card</title>
<link href="https://fonts.googleapis.com/css2?family=Didact+Gothic&display=swap" rel="stylesheet">
<style>
  :root {
    --paper: #ffffff;
    --card-black: #141414;
    --deep-black: #080808;
    --panel-grey: #888a89;
    --silver: #9a9a9a;
    --dark-grey: #5f605f;
    --accent-red: #e0252a;
    --ink: #111111;
    --white: #ffffff;
  }
  * { margin: 0; padding: 0; box-sizing: border-box; }
  html, body {
    width: 1200px; height: 1200px; overflow: hidden;
    background: var(--paper);
    font-family: "Didact Gothic", sans-serif;
  }
  .canvas { position: relative; width: 1200px; height: 1200px; }

  /* Front side */
  .card-front {
    position: absolute; left: 266px; top: 84px;
    width: 840px; height: 480px;
  }
  .card-front svg { display: block; }
  .brand-name {
    font-family: "Didact Gothic", sans-serif;
    font-size: 40px; fill: var(--silver);
  }

  /* Back side */
  .card-back {
    position: absolute; left: 102px; top: 636px;
    width: 840px; height: 480px;
    background: var(--card-black);
    color: var(--white);
  }
  .website {
    position: absolute; right: 42px; top: 14px;
    font-size: 22px; letter-spacing: 0.2px;
  }
  .photo-panel {
    position: absolute; left: 43px; top: 46px;
    width: 755px; height: 309px;
    background: var(--panel-grey);
  }
  .focus-frame {
    position: absolute; left: 321px; top: 98px;
  }
  .contact-list {
    position: absolute; right: 27px; top: 180px;
    list-style: none;
    color: var(--ink); font-size: 22px;
  }
  .contact-item {
    display: flex; justify-content: flex-end; align-items: center;
    gap: 12px; height: 39px;
  }
  .contact-icon {
    width: 26px; height: 26px; border-radius: 3px;
    background: var(--accent-red);
    display: flex; align-items: center; justify-content: center;
  }
  .person-name {
    position: absolute; left: 42px; top: 358px;
    font-size: 66px; line-height: 1; letter-spacing: 0.5px;
  }
  .name-rule {
    position: absolute; left: 40px; top: 421px;
    width: 758px; height: 3px;
    background: var(--accent-red);
  }
  .role {
    position: absolute; right: 42px; top: 426px;
    font-size: 32px; line-height: 1.2;
  }
</style>
</head>
<body>
<main class="canvas">

  <section class="card-front">
    <svg width="840" height="480" viewBox="0 0 840 480">
      <defs>
        <linearGradient id="camera-tones" x1="0" y1="0" x2="0" y2="1">
          <stop offset="0" stop-color="#080808"/>
          <stop offset="0.2" stop-color="#9a9a9a"/>
          <stop offset="0.5" stop-color="#0c0c0c"/>
          <stop offset="0.8" stop-color="#9a9a9a"/>
          <stop offset="1" stop-color="#8a8a8a"/>
        </linearGradient>
      </defs>
      <rect class="camera-art" width="840" height="480" fill="url(#camera-tones)"
            role="img" aria-label="Flat illustration of a camera body in black and grey"/>
      <circle cx="482" cy="268" r="170" fill="var(--deep-black)" stroke="var(--white)" stroke-width="10"/>
      <text class="brand-name" x="482" y="282" text-anchor="middle">Gavin Tolley</text>
    </svg>
  </section>

  <section class="card-back">
    <div class="website">www.GavinTolleyPhotography.com.au</div>
    <div class="photo-panel">
      <svg class="focus-frame" width="114" height="114" viewBox="0 0 114 114" fill="none" stroke="#111" stroke-width="1.3">
        <path d="M1 42V1H42M72 1H113V42M113 72V113H72M42 113H1V72"/>
      </svg>
      <ul class="contact-list">
        <li class="contact-item">0482615073
          <span class="contact-icon">
            <svg width="18" height="18" viewBox="0 0 24 24" fill="none" stroke="#fff" stroke-width="2" stroke-linejoin="round">
              <path d="M5 3h4l2 5-2.5 1.5a11 11 0 0 0 6 6L16 13l5 2v4a2 2 0 0 1-2 2A17 17 0 0 1 3 5a2 2 0 0 1 2-2z"/>
            </svg>
          </span>
        </li>
        <li class="contact-item">Gavin_tolley
          <span class="contact-icon"></span>
        </li>
        <li class="contact-item">GavinTolleyPhotography82@lumenpost.com
          <span class="contact-icon">
            <svg width="18" height="14" viewBox="0 0 18 14" fill="none" stroke="#fff" stroke-width="1.6">
              <rect x="1" y="1" width="16" height="12"/>
              <path d="M1 1l8 7 8-7M1 13l6-6M17 13l-6-6"/>
            </svg>
          </span>
        </li>
      </ul>
    </div>
    <h1 class="person-name">Gavin Tolley</h1>
    <div class="name-rule"></div>
    <p class="role">photographer</p>
  </section>

</main>
</body>
</html>
```